Sophisticated & Clean Comedy Show Flyer

Pale Harbor Entertainment, a talent management company, is producing a showcase to introduce their comedians to the industry. The design should be clean and sophisticated and introduce a graphical element that evokes comedy, without being cheesy.

I have attached the following files:
* Pale Harbor Logo - file #1
* Copy for flyer - file #2
* textured business card for Pale Harbor Entertainment for design reference - file #3
* example of a comedy flyer with graphic and texture that is clean and sophisticated and fun. - file #4

Industry/Entity Type

Entertainment Industry

Font styles to use
Sans Serif

Colors
000000
ffffff
e8e8e8

Requirements
Must have
• Logo ad all the content listed in the file #2
Nice to have
• A graphical element that evokes comedy that is not generic or cheesy
• I don't mind accent color on the flyer - but overall it should be clean look

```html
<!DOCTYPE html>
<html lang="en">
<head>
<meta charset="UTF-8">
<title>Comedy Showcase – Pale Harbor Entertainment</title>
<link href="https://fonts.googleapis.com/css2?family=Archivo+Black&family=Patrick+Hand+SC&display=swap" rel="stylesheet">
<style>
  :root {
    --ink: #000000;
    --paper: #ffffff;
    --mist: #e8e8e8;
    --accent: #f05a2a;
    --wash-purple: #c99be0;
    --wash-blue: #9fd0ee;
    --wash-pink: #f6b7c4;
    --wash-green: #cde6a8;
    --wash-yellow: #fbe3a4;
  }
  * { margin: 0; padding: 0; box-sizing: border-box; }
  html, body { width: 849px; height: 1200px; overflow: hidden; background: var(--paper); }
  .flyer {
    position: relative;
    width: 849px;
    height: 1200px;
    background: var(--paper);
    color: var(--ink);
    font-family: "Patrick Hand SC", sans-serif;
    overflow: hidden;
  }
  .brand {
    position: absolute;
    top: 30px; left: 0; width: 100%;
    text-align: center;
    font-family: "Archivo Black", sans-serif;
    line-height: 1;
  }
  .brand-name { font-size: 58px; letter-spacing: -1px; text-transform: uppercase; }
  .brand-sub { font-size: 22px; letter-spacing: 2px; text-transform: uppercase; margin-top: 4px; }
  .title {
    position: absolute;
    top: 196px; left: 0; width: 100%;
    text-align: center;
    font-size: 90px;
    font-weight: 400;
    color: var(--accent);
    letter-spacing: 4px;
    line-height: 1;
  }
  .host {
    position: absolute;
    top: 302px; left: 0; width: 100%;
    text-align: center;
    line-height: 1;
  }
  .host-label { font-size: 40px; }
  .host-name { font-size: 54px; margin-top: 2px; letter-spacing: 2px; }
  .host-credit { font-size: 32px; margin-top: 2px; }
  .artwork {
    position: absolute;
    top: 450px; left: 80px;
    width: 690px; height: 500px;
    border-radius: 40% 45% 38% 42%;
    background:
      radial-gradient(circle at 32% 40%, var(--wash-purple) 0 22%, transparent 45%),
      radial-gradient(circle at 66% 42%, var(--wash-blue) 0 22%, transparent 45%),
      radial-gradient(circle at 50% 78%, var(--wash-pink) 0 15%, transparent 40%),
      radial-gradient(circle at 82% 74%, var(--wash-green) 0 12%, transparent 35%),
      radial-gradient(circle at 20% 20%, var(--wash-yellow) 0 12%, transparent 35%),
      var(--paper);
    opacity: 0.85;
  }
  .lineup {
    position: absolute;
    top: 790px; left: 62px;
    list-style: none;
    font-size: 27px;
    line-height: 1;
  }
  .lineup-label { font-size: 23px; }
  .lineup-credit { font-size: 22px; }
  .date {
    position: absolute;
    top: 996px; left: 52px;
    color: var(--accent);
    font-size: 42px;
    line-height: 0.95;
    text-align: center;
  }
  .times {
    position: absolute;
    top: 1016px; left: 566px;
    color: var(--accent);
    font-size: 44px;
    line-height: 1;
  }
  .venue-band {
    position: absolute;
    bottom: 0; left: 0;
    width: 100%; height: 74px;
    background: var(--ink);
    color: var(--paper);
    font-size: 30px;
    display: flex;
    align-items: center;
    justify-content: center;
    letter-spacing: 1px;
  }
</style>
</head>
<body>
  <main class="flyer">
    <header class="brand">
      <div class="brand-name">Pale Harbor</div>
      <div class="brand-sub">Entertainment</div>
    </header>

    <h1 class="title">COMEDY SHOWCASE</h1>

    <section class="host">
      <div class="host-label">Hosted by</div>
      <div class="host-name">DEXTER MALONE</div>
      <div class="host-credit">(Laugh Channel)</div>
    </section>

    <div class="artwork" role="img" aria-label="Watercolour splash in purple, blue, pink and green behind a pair of comedy and tragedy theatre masks"></div>

    <ul class="lineup">
      <li class="lineup-label">Featuring</li>
      <li>NINA VALDEZ <span class="lineup-credit">(Laugh Channel, Tune Two)</span></li>
      <li>OSCAR PRUITT <span class="lineup-credit">(Arc TV, Vixen Net)</span></li>
      <li>LENA WHITFIELD <span class="lineup-credit">(Arc TV)</span></li>
      <li>GRANT SORENSEN <span class="lineup-credit">(Surfside, Arc TV)</span></li>
      <li>FELIX ARDMORE <span class="lineup-credit">(Harbor City Comedy Festival)</span></li>
    </ul>

    <div class="date">MONDAY,<br>NOVEMBER<br>16TH</div>

    <div class="times">Doors 7PM<br>Show 7:30PM</div>

    <footer class="venue-band">LINWOOD 318 W 22ND STREET, NY, NY 10020</footer>
  </main>
</body>
</html>
```